Hollis Row Pantry Business Cards
Hollis Row Pantry
Hollis Row Pantry Business Cards - Food
Creative Brief
Use specific fonts
Designer choice to compliment font used in logo
Professional
Mirela Vance
Store Manager
482 W Tamarind Ave Brennick Falls, VT 05921
mirela@hollisrowpantry.example
www.HollisRowPantry.example

```html
<!DOCTYPE html>
<html lang="en">
<head>
<meta charset="utf-8">
<title>Hollis Row Pantry Business Cards</title>
<link rel="stylesheet" href="https://fonts.googleapis.com/css2?family=Cinzel:wght@400;600&family=Open+Sans:wght@400&display=swap">
<style>
  :root {
    --backdrop: #3b332e;
    --card: #1f1f20;
    --card-edge: #2a2a2b;
    --ink: #e9e9e9;
    --ink-soft: #cfcfcf;
    --silver-light: #f2f2f2;
    --silver-dark: #8a8a8a;
  }
  * { box-sizing: border-box; margin: 0; padding: 0; }
  html, body { width: 1200px; height: 769px; overflow: hidden; background: var(--backdrop); }
  .canvas {
    position: relative; width: 1200px; height: 769px;
    display: flex; align-items: center; justify-content: center; gap: 60px;
  }
  .card {
    position: relative; width: 500px; height: 286px;
    background: var(--card); border: 1px solid var(--card-edge);
    box-shadow: 0 10px 24px rgba(0,0,0,.45);
    color: var(--ink);
  }
  /* front */
  .brand-block {
    position: absolute; left: 30px; top: 60px; width: 200px;
    display: flex; flex-direction: column; align-items: center;
  }
  .brand-mark {
    width: 70px; height: 70px; border-radius: 50%;
    background: var(--ink); margin-bottom: 10px;
  }
  .brand-rule {
    width: 190px; height: 0; border-top: 1.5px solid var(--ink); margin-bottom: 10px;
  }
  .brand-name {
    font-family: "Cinzel", serif; font-weight: 400; font-size: 24px;
    line-height: 1.15; letter-spacing: 1px; text-align: center; color: var(--ink);
  }
  .details {
    position: absolute; left: 250px; top: 50px; width: 235px;
    font-family: "Open Sans", sans-serif; font-size: 12.5px; color: var(--ink-soft);
  }
  .person {
    font-family: "Cinzel", serif; font-weight: 600; font-size: 17px;
    letter-spacing: .5px; color: var(--ink); line-height: 1.1;
  }
  .role {
    font-family: "Cinzel", serif; font-weight: 400; font-size: 12.5px;
    letter-spacing: .5px; color: var(--ink); margin-bottom: 10px;
  }
  .address { line-height: 1.5; margin-bottom: 8px; }
  .contact-list { list-style: none; }
  .contact-list li { display: flex; align-items: center; gap: 8px; line-height: 1.55; white-space: nowrap; }
  .contact-list svg { width: 12px; height: 12px; flex: none; fill: none; stroke: var(--ink-soft); stroke-width: 1.4; }
  /* back */
  .back { display: flex; flex-direction: column; align-items: center; justify-content: center; }
  .back-mark {
    width: 120px; height: 120px; border-radius: 50%;
    background: radial-gradient(circle at 35% 30%, var(--silver-light), var(--silver-dark));
    margin-bottom: 18px;
  }
  .back-name {
    font-family: "Cinzel", serif; font-weight: 400; font-size: 18px;
    letter-spacing: 1.5px; color: var(--ink); margin-bottom: 12px;
  }
  .back-url {
    font-family: "Cinzel", serif; font-size: 12px; letter-spacing: 1px; color: var(--ink-soft);
  }
</style>
</head>
<body>
<main class="canvas">
  <section class="card front">
    <div class="brand-block">
      <div class="brand-mark"></div>
      <div class="brand-rule"></div>
      <div class="brand-name">Hollis Row Pantry</div>
    </div>
    <div class="details">
      <div class="person">Mirela Vance</div>
      <div class="role">Store Manager</div>
      <div class="address">482 W Tamarind Ave<br>Brennick Falls, VT 05921</div>
      <ul class="contact-list">
        <li><svg viewBox="0 0 12 12"><path d="M2 4c0-1.5 2-2.5 4-2.5s4 1 4 2.5M3 5h6l1 5H2z"/></svg>419-555-0142</li>
        <li><svg viewBox="0 0 12 12"><rect x="3" y="1" width="6" height="10" rx="1"/><path d="M5.5 9h1"/></svg>419-555-0187</li>
        <li><svg viewBox="0 0 12 12"><rect x="1" y="3" width="10" height="7"/><path d="M1 3l5 4 5-4"/></svg>mirela@hollisrowpantry.example</li>
        <li><svg viewBox="0 0 12 12"><circle cx="6" cy="6" r="4.6"/><path d="M1.4 6h9.2M6 1.4c-2 2.5-2 6.7 0 9.2M6 1.4c2 2.5 2 6.7 0 9.2"/></svg>www.HollisRowPantry.example</li>
      </ul>
    </div>
  </section>
  <section class="card back">
    <div class="back-mark"></div>
    <div class="back-name">Hollis Row Pantry</div>
    <div class="back-url">www.HollisRowPantry.example</div>
  </section>
</main>
</body>
</html>
```